New Zealand Marlborough Sauvignon Blanc wine packaging design

We need packaging design for our new wine brand, Dunmore Hale. The wine is a New Zealand Marlborough Sauvignon Blanc. We would like the packaging will portray elegance and style with an understated label. We are looking for a label that portrays the elegance of the French Riviera. The label should be round or pill shaped.
Updates

Industry/Entity Type

Wine

Font styles to use
Serif
Sans Serif

Requirements
Must have
• The words in order of importance: Dunmore Hale, Sauvignon Blanc, Marlborough, New Zealand. It should be fit to the bottle posted in the links
Nice to have
• a pill shape or circular shape
Should not have
• Illustrations of wine bottles, wine glasses, or grapes

```html
<!DOCTYPE html>
<html lang="en">
<head>
<meta charset="utf-8">
<title>Dunmore Hale – Marlborough Sauvignon Blanc</title>
<link rel="stylesheet" href="https://fonts.googleapis.com/css2?family=EB+Garamond:wght@400&family=Norican&display=swap">
<style>
  :root {
    --paper: #ffffff;
    --glass-edge: #1f0608;
    --glass-mid: #3a1c1d;
    --label-line: #c8643a;
    --copper: #b14a2a;
    --copper-light: #ec8a55;
    --copper-deep: #9a2a22;
    --sea: #b3d9e6;
    --mist: #dce9f4;
    --ink: #5a4440;
  }
  html, body {
    margin: 0;
    padding: 0;
    width: 849px;
    height: 1200px;
    overflow: hidden;
    background: var(--paper);
  }
  .canvas {
    display: block;
    width: 849px;
    height: 1200px;
  }
  .region-text {
    font-family: "EB Garamond", Georgia, serif;
    font-size: 14px;
    letter-spacing: 2.4px;
    fill: var(--ink);
  }
  .brand-name {
    font-family: "Norican", "Brush Script MT", cursive;
    font-size: 42px;
    fill: var(--copper);
  }
  .variety {
    font-family: "EB Garamond", Georgia, serif;
    font-size: 18px;
    letter-spacing: 0.5px;
    fill: var(--paper);
  }
</style>
</head>
<body>
<svg class="canvas" viewBox="0 0 849 1200" xmlns="http://www.w3.org/2000/svg">
  <defs>
    <linearGradient id="glass" x1="0" x2="1" y1="0" y2="0">
      <stop offset="0" stop-color="var(--glass-edge)"/>
      <stop offset="0.2" stop-color="var(--glass-mid)"/>
      <stop offset="0.8" stop-color="var(--glass-mid)"/>
      <stop offset="1" stop-color="var(--glass-edge)"/>
    </linearGradient>
    <linearGradient id="landscape" x1="0" y1="1" x2="1" y2="0">
      <stop offset="0" stop-color="var(--sea)"/>
      <stop offset="0.45" stop-color="var(--mist)"/>
      <stop offset="0.5" stop-color="var(--copper)"/>
      <stop offset="0.8" stop-color="var(--copper-light)"/>
      <stop offset="1" stop-color="var(--copper-deep)"/>
    </linearGradient>
    <linearGradient id="bowl" x1="0" y1="0.2" x2="1" y2="0.8">
      <stop offset="0" stop-color="var(--copper-light)"/>
      <stop offset="0.5" stop-color="var(--copper)"/>
      <stop offset="1" stop-color="var(--copper-deep)"/>
    </linearGradient>
    <path id="arc-top" d="M345,790 A95,95 0 0 1 505,790"/>
    <path id="arc-bottom" d="M352,1034 A95,95 0 0 0 497,1034"/>
  </defs>

  <g class="bottle">
    <path class="bottle-cap" fill="var(--glass-mid)"
      d="M374,33 H476 Q479,33 479,37 V48 Q482,50 479,53 V58 Q482,60 479,63 V73 Q481,74 481,78 L482,116 H368 L369,78 Q369,74 371,73 V63 Q368,60 371,58 V53 Q368,50 371,48 V37 Q371,33 374,33 Z"/>
    <path class="bottle-body" fill="url(#glass)"
      d="M372,116 H477 L479,240 C481,300 484,360 492,420 C508,520 550,540 570,600 C578,630 579,660 579,680 L579,1150 Q579,1171 563,1171 L286,1171 Q270,1171 270,1150 L270,680 C270,660 271,630 279,600 C299,540 341,520 357,420 C365,360 368,300 370,240 Z"/>
    <line class="label-edge" x1="270" y1="681" x2="579" y2="681" stroke="#6b4a48" stroke-width="0.6"/>
    <line class="label-edge" x1="270" y1="1113" x2="579" y2="1113" stroke="#6b4a48" stroke-width="0.6"/>
  </g>

  <g class="label">
    <rect class="label-pill" x="288" y="715" width="273" height="363" rx="136" ry="150" fill="var(--paper)"/>
    <rect class="label-rule" x="292" y="719" width="265" height="355" rx="132" ry="146" fill="none" stroke="var(--label-line)" stroke-width="0.8"/>

    <text class="region-text"><textPath href="#arc-top" startOffset="50%" text-anchor="middle">MARLBOROUGH</textPath></text>

    <path class="landscape" role="img" aria-label="Stylised illustration of Marlborough coastline hills and sea"
      d="M322,895 V858 A102.5,102.5 0 0 1 527,858 V895 Z" fill="url(#landscape)"/>

    <text class="brand-name" x="424.5" y="932" text-anchor="middle">Dunmore Hale</text>

    <path class="variety-band" d="M325,955 H526 A100.5,88 0 0 1 325,955 Z" fill="url(#bowl)"/>
    <text class="variety" x="424.5" y="998" text-anchor="middle">Sauvignon Blanc</text>

    <text class="region-text"><textPath href="#arc-bottom" startOffset="50%" text-anchor="middle">NEW ZEALAND</textPath></text>
  </g>
</svg>
</body>
</html>
```